Junk Removal company with existing WordPress website needs new mobile enhanced website

I am looking to have someone take my existing website and either update it with a new design and menu which is more mobile enhanced (70% of my traffic is from mobile devices and most people stay on the home page to find what they need) or create a new website from scratch to achieve my design goals. My name goal is the have to home page be quick and easy to find what the customer is looking for.
Our current website is: BrightCreekJunkOut.com and Localy my business page https://g.page/brightcreekjunkout
I have attached an example the design idea I came up with for the home page based on what I would like it to look like as well as some logo files and pictures.

```html
<!DOCTYPE html>
<html lang="en">
<head>
<meta charset="utf-8">
<title>Bright Creek Junk Out – Home Page Design</title>
<link href="https://fonts.googleapis.com/css2?family=Oswald:wght@300;400;500;600;700&family=Poppins:wght@400;500;600;700&family=Montserrat:wght@800&display=swap" rel="stylesheet">
<style>
:root{
  --board:#2f2f2f;
  --board-hi:#3a3a3a;
  --dark:#2e2e2e;
  --orange:#f26a1b;
  --red:#f0441c;
  --amber:#ffb300;
  --ink:#2b2b2b;
  --muted:#6b6b6b;
  --light:#ffffff;
  --line:#e3e3e3;
  --sky:#c9d7ea;
}
*{box-sizing:border-box;margin:0;padding:0}
html,body{width:1200px;height:3354px;overflow:hidden}
body{position:relative;background:linear-gradient(135deg,var(--board) 0%,var(--board-hi) 35%,var(--board) 60%,var(--board-hi) 100%);font-family:'Poppins',sans-serif;color:var(--ink)}
.abs{position:absolute}
.brand-title{position:absolute;left:0;width:1200px;top:150px;text-align:center;font-family:'Oswald',sans-serif;font-weight:600;font-size:54px;letter-spacing:3px;color:var(--light)}
.brand-title .dot{display:inline-block;width:26px;height:26px;border-radius:50%;background:var(--orange);margin-right:18px;vertical-align:middle}
.board-label{position:absolute;top:380px;font-family:'Montserrat',sans-serif;font-weight:800;font-size:34px;color:var(--light);letter-spacing:.5px}
.frame{position:absolute;top:424px;background:var(--light);overflow:hidden;box-shadow:0 20px 40px rgba(0,0,0,.45)}
.desktop{left:200px;width:585px;height:2305px}
.mobile{left:839px;width:161px;height:2808px}
.photo{position:absolute}
.hero-photo{background:linear-gradient(180deg,#d7e2f1 0%,#c3d3e8 35%,#aab6c4 55%,#3a3d43 68%,#5f6a4c 82%,#7b8456 100%)}
.truck-photo{background:linear-gradient(160deg,#cfd6df 0%,#8d97a3 45%,#2a2c30 75%,#555 100%)}
.map-photo{background:linear-gradient(150deg,#eef0e4 0%,#dde6d4 45%,#cfdbe8 100%)}
.hex{clip-path:polygon(25% 0,75% 0,100% 50%,75% 100%,25% 100%,0 50%)}
.hexv{clip-path:polygon(50% 0,100% 25%,100% 75%,50% 100%,0 75%,0 25%)}
.logo-text{position:absolute;font-family:'Oswald',sans-serif;font-weight:600;color:var(--light);text-align:center;line-height:1.05;letter-spacing:.5px}
.logo-text.on-light{color:var(--ink)}
.tiny{font-size:5.5px;line-height:1.35;color:var(--muted)}
.call-label{font-size:6px;font-weight:600;color:var(--ink)}
.phone-pill{position:absolute;background:var(--dark);color:var(--light);border-radius:20px;display:flex;align-items:center;font-weight:600;letter-spacing:.5px}
.phone-pill .ic{background:var(--light);border-radius:50%;display:flex;align-items:center;justify-content:center}
.hours{font-size:6px;font-weight:600;line-height:1.2;color:var(--ink)}
.burger span{display:block;height:2px;background:var(--ink);margin-bottom:4px}
.banner{position:absolute;background:var(--orange);color:var(--light);font-family:'Oswald',sans-serif;font-weight:300;text-align:center;display:flex;align-items:center;justify-content:center;text-transform:uppercase}
.review-mark{position:absolute;border-radius:50%;background:var(--orange)}
.review-name{position:absolute;font-weight:600;color:#555;line-height:1.3}
.stars{position:absolute;color:var(--amber);letter-spacing:1px}
.score{position:absolute;font-weight:700;color:var(--ink)}
.pill-dark{position:absolute;background:#444;color:var(--light);border-radius:20px;font-weight:600;text-align:center;text-transform:uppercase}
.rule{position:absolute;height:1px;background:var(--line)}
.card{position:absolute;background:var(--light);box-shadow:0 2px 8px rgba(0,0,0,.18)}
.card h4{position:absolute;left:8px;top:9px;font-family:'Oswald',sans-serif;font-weight:500;font-size:7px;color:var(--ink);text-transform:uppercase}
.card .cicon{position:absolute;right:8px;top:7px}
.card .cphoto{position:absolute;left:0;top:28px;width:100%;height:86px;background:linear-gradient(170deg,#9fb4c7,#6d7d8c 60%,#4a4f55)}
.card ul{position:absolute;left:12px;top:124px;list-style:none}
.card li{font-size:5.5px;line-height:1.72;color:var(--muted)}
.card li::before{content:"";display:inline-block;width:3px;height:3px;border:1px solid var(--orange);border-radius:50%;margin-right:3px;vertical-align:middle}
.card .cbtn{position:absolute;left:18px;right:18px;bottom:14px;height:19px;border-radius:12px;background:#e6e6e6;font-size:4.5px;font-weight:600;color:#333;text-align:center;display:flex;align-items:center;justify-content:center;line-height:1.2;text-transform:uppercase}
.dark-band{position:absolute;left:0;background:var(--dark)}
.sec-title{position:absolute;font-family:'Oswald',sans-serif;font-weight:300;text-transform:uppercase;color:var(--ink)}
.sec-title.on-dark{color:var(--light)}
.price-item{position:absolute}
.price-item h5{font-family:'Oswald',sans-serif;font-weight:500;font-size:7px;color:var(--light);text-transform:uppercase;margin-bottom:2px}
.price-item p{font-size:5.5px;line-height:1.4;color:#cfcfcf}
.pi-icon{position:absolute}
.step-num{position:absolute;font-family:'Oswald',sans-serif;font-weight:700;color:#e4e4e4}
.step h5{font-family:'Oswald',sans-serif;font-weight:500;font-size:7.5px;text-transform:uppercase;color:var(--ink);margin-bottom:2px}
.step{position:absolute}
.btn{position:absolute;border-radius:10px;color:var(--light);font-weight:700;text-align:center;text-transform:uppercase;display:flex;align-items:center;justify-content:center}
.btn.red{background:var(--red)}
.btn.amber{background:var(--amber)}
.deco-hex{position:absolute;background:var(--amber)}
.body-copy{position:absolute;font-size:6.5px;line-height:1.6;color:var(--muted)}
.compare{position:absolute;display:flex;align-items:center}
.compare .truck{background:linear-gradient(180deg,#eee,#555 60%,#222);border-radius:2px}
.compare .spec{font-family:'Oswald',sans-serif;font-weight:500;color:var(--ink);line-height:1.25;text-transform:uppercase}
.vdiv{position:absolute;width:1px;background:var(--line)}
.area-list{position:absolute;list-style:none}
.area-list li{font-size:6.5px;line-height:1.8;color:var(--muted)}
.area-list li::before{content:"";display:inline-block;width:3px;height:3px;border:1px solid var(--orange);border-radius:50%;margin-right:4px;vertical-align:middle}
.link-orange{position:absolute;font-size:6px;font-weight:700;color:var(--orange);text-decoration:underline;text-transform:uppercase}
.pin-hex{position:absolute;background:var(--amber);display:flex;align-items:center;justify-content:center}
.cta-band{position:absolute;background:var(--orange)}
.cta-text{position:absolute;font-family:'Oswald',sans-serif;font-weight:300;color:var(--light);text-transform:uppercase;line-height:1.1}
.btn-white{position:absolute;background:var(--light);color:var(--ink);border-radius:12px;font-weight:700;text-transform:uppercase;display:flex;align-items:center;justify-content:center}
.foot-col{position:absolute}
.foot-col h6{font-family:'Oswald',sans-serif;font-weight:500;color:var(--light);text-transform:uppercase;margin-bottom:5px}
.foot-col ul{list-style:none}
.foot-col li{color:#cfcfcf;line-height:1.8}
.foot-col li::before{content:"";display:inline-block;width:3px;height:3px;border:1px solid var(--orange);border-radius:50%;margin-right:4px;vertical-align:middle}
.contact-row{display:flex;gap:6px;align-items:flex-start;margin-bottom:8px;color:var(--light)}
.contact-row small{display:block;color:#aaa}
.copyright{position:absolute;left:0;width:100%;text-align:center;font-family:'Oswald',sans-serif;font-weight:400;color:#ddd;text-transform:uppercase}
.to-top{position:absolute;background:var(--amber);border-radius:4px;display:flex;align-items:center;justify-content:center}
.arrow-btn{position:absolute;width:17px;height:17px;border-radius:50%;background:#e2e2e2;display:flex;align-items:center;justify-content:center}
</style>
</head>
<body>

<div class="brand-title"><span class="dot"></span>BRIGHT CREEK JUNK OUT</div>

<div class="board-label" style="left:199px">DESKTOP</div>
<div class="board-label" style="left:837px">MOBILE</div>

<!-- ================= DESKTOP ================= -->
<section class="frame desktop">
  <div class="photo hero-photo" style="left:0;top:0;width:585px;height:366px" role="img" aria-label="Photo of the company's box trucks, pickup and dumpster trailer parked in a row"></div>

  <div class="burger abs" style="left:45px;top:77px;width:20px"><span></span><span style="width:14px"></span><span></span></div>
  <div class="hours abs" style="left:82px;top:77px">MON TO SAT<br>8AM TO 6PM</div>

  <div class="logo-text on-light" style="left:210px;top:60px;width:166px;font-size:22px">BRIGHT CREEK<br>JUNK OUT</div>

  <div class="call-label abs" style="left:422px;top:61px">CLICK TO CALL</div>
  <div class="phone-pill" style="left:422px;top:72px;width:118px;height:23px;font-size:11px">
    <span class="ic" style="width:17px;height:17px;margin:0 9px 0 3px">
      <svg width="10" height="10" viewBox="0 0 24 24"><path fill="#f26a1b" d="M6.6 10.8a15.2 15.2 0 0 0 6.6 6.6l2.2-2.2c.3-.3.7-.4 1-.2 1.1.4 2.3.6 3.6.6.6 0 1 .4 1 1V20c0 .6-.4 1-1 1A17 17 0 0 1 3 4c0-.6.4-1 1-1h3.5c.6 0 1 .4 1 1 0 1.3.2 2.5.6 3.6.1.3 0 .7-.2 1z"/></svg>
    </span>208-555-0147
  </div>

  <div class="banner" style="left:43px;top:328px;width:497px;height:76px;font-size:15px;line-height:1.3">
    <span class="abs" style="left:40px;top:38px;width:40px;height:1px;background:#fff"></span>
    Best rated junk removal &amp; property cleanout<br>company in the Bright Creek Valley
    <span class="abs" style="right:40px;top:38px;width:40px;height:1px;background:#fff"></span>
  </div>

  <div class="review-mark" style="left:117px;top:437px;width:42px;height:42px"></div>
  <div class="review-name" style="left:170px;top:442px;font-size:13px">Localy<br>Business Review</div>
  <div class="score" style="left:121px;top:483px;font-size:18px">5.0</div>
  <div class="stars" style="left:170px;top:486px;font-size:13px">★★★★<span style="color:#ddd">★</span></div>
  <div class="pill-dark" style="left:300px;top:461px;width:167px;height:22px;line-height:22px;font-size:7px">Fast, friendly &amp; professionals...</div>

  <div class="rule" style="left:43px;top:536px;width:497px"></div>

  <div class="dark-band" style="top:834px;width:585px;height:294px"></div>

  <article class="card" style="left:43px;top:582px;width:120px;height:289px">
    <h4>Junk Removal</h4>
    <svg class="cicon" width="22" height="14" viewBox="0 0 22 14"><rect x="1" y="3" width="12" height="7" fill="none" stroke="#2b2b2b"/><path d="M13 5h5l3 3v2h-8z" fill="none" stroke="#2b2b2b"/><circle cx="5" cy="11.5" r="1.8" fill="#f26a1b"/><circle cx="17" cy="11.5" r="1.8" fill="#f26a1b"/></svg>
    <div class="cphoto" role="img" aria-label="Photo of old appliances set out for pickup"></div>
    <ul><li>Misc. Household Junk</li><li>Furniture Removal</li><li>Mattress Removal</li><li>Appliance Removal</li><li>Hot Tub Removal</li><li>Yard Debris Removal</li><li>Remodeling Debris</li><li>Construction Debris</li><li>Play Structure Removal</li><li>Shed Removal</li></ul>
    <div class="cbtn">Same &amp; next day<br>service available</div>
  </article>
  <article class="card" style="left:169px;top:582px;width:120px;height:289px">
    <h4>Property Cleanout</h4>
    <svg class="cicon" width="16" height="14" viewBox="0 0 16 14"><path d="M1 7L8 1l7 6v6H1z" fill="none" stroke="#2b2b2b"/><rect x="6" y="8" width="4" height="5" fill="#f26a1b"/></svg>
    <div class="cphoto" style="background:linear-gradient(170deg,#b9c4cf,#8b7d6c 55%,#5b4b3c)" role="img" aria-label="Photo of a house yard piled with items from a cleanout"></div>
    <ul><li>Estate Cleanout</li><li>Residential Cleanout</li><li>Garage Cleanout</li><li>Storage Unit Cleanout</li><li>Foreclosure Cleanout</li><li>Hoarder Cleanout</li><li>Attic Cleanout</li><li>Basement Cleanout</li><li>Business Cleanout</li><li>Office Cleanout</li><li>Mobile Home Cleanout</li><li>House Cleanout</li></ul>
    <div class="cbtn">We do all the hard work<br>so you don't have to!</div>
  </article>
  <article class="card" style="left:295px;top:582px;width:120px;height:289px">
    <h4>Light Demolition</h4>
    <svg class="cicon" width="16" height="14" viewBox="0 0 16 14"><rect x="1" y="6" width="8" height="7" fill="none" stroke="#2b2b2b"/><path d="M8 5l6-4M12 2l2 3" stroke="#f26a1b" stroke-width="1.5" fill="none"/></svg>
    <div class="cphoto" style="background:linear-gradient(170deg,#aac0d6,#7d8f6c 55%,#5a6b43)" role="img" aria-label="Photo of a wooden backyard play structure"></div>
    <ul><li>Shed Removal</li><li>Fence Removal</li><li>Deck Removal</li><li>Hot Tub Removal</li><li>Play Structure Removal</li><li>Swing Set Removal</li><li>Gazebo Removal</li><li>Above-Ground Pool</li><li>Misc. Small Structures</li></ul>
    <div class="cbtn">Same &amp; next day<br>service available</div>
  </article>
  <article class="card" style="left:422px;top:582px;width:120px;height:289px">
    <h4>Dumpster Rental</h4>
    <svg class="cicon" width="22" height="14" viewBox="0 0 22 14"><path d="M2 4h14l-2 7H4z" fill="none" stroke="#2b2b2b"/><circle cx="6" cy="12" r="1.6" fill="#f26a1b"/><circle cx="13" cy="12" r="1.6" fill="#f26a1b"/><path d="M16 8h5" stroke="#2b2b2b"/></svg>
    <div class="cphoto" style="background:linear-gradient(170deg,#c3ccd6,#4a4e55 55%,#2a2c30)" role="img" aria-label="Photo of a black dumpster trailer in a driveway"></div>
    <ul><li>Flat Free Pricing</li><li>Driveway Safe Dumpster</li><li>14 Cubic Yard Capacity</li><li>24hr, 48hr, 72hr or Weekly</li><li>&nbsp;&nbsp;Rentals Available</li><li>Delivery &amp; Pickup Includes</li><li>2 Tons Disposal Fee Included</li></ul>
    <div class="cbtn">Would you prefer to<br>do-it-yourself?</div>
  </article>

  <h2 class="sec-title on-dark" style="left:0;width:585px;text-align:center;top:920px;font-size:16px">How We Price</h2>
  <div class="logo-text" style="left:228px;top:1000px;width:128px;font-size:17px">BRIGHT CREEK<br>JUNK OUT</div>

  <div class="price-item" style="left:40px;top:963px;width:128px;text-align:right"><h5>Volume Based Pricing</h5><p>Our pricing is based on the amount of space your items take up in our truck.</p></div>
  <div class="price-item" style="left:40px;top:1009px;width:128px;text-align:right"><h5>Free Estimates</h5><p>We can provide a free estimate over the phone, text or email so you know a price range before we show up.</p></div>
  <div class="price-item" style="left:40px;top:1061px;width:128px;text-align:right"><h5>No Hidden Fees</h5><p>All fuel, labor and disposal fees are included in your upfront pricing.</p></div>
  <div class="price-item" style="left:415px;top:963px;width:130px"><h5>Minimum Loads</h5><p>Our pricing starts at a minimum pickup fee and goes up through twelve different price points to a full load rate.</p></div>
  <div class="price-item" style="left:415px;top:1015px;width:130px"><h5>Upfront Pricing</h5><p>We always provide our valued customers with a firm price on-site before we begin a job.</p></div>

  <svg class="pi-icon" style="left:176px;top:962px" width="26" height="26" viewBox="0 0 26 26"><rect x="3" y="5" width="20" height="16" fill="none" stroke="#f26a1b" stroke-width="1.5"/><path d="M7 10h12M7 14h8" stroke="#f26a1b" stroke-width="1.5"/></svg>
  <svg class="pi-icon" style="left:176px;top:1008px" width="26" height="26" viewBox="0 0 26 26"><circle cx="13" cy="13" r="9" fill="none" stroke="#f26a1b" stroke-width="1.5"/><path d="M13 8v10M10 11h6" stroke="#f26a1b" stroke-width="1.5"/></svg>
  <svg class="pi-icon" style="left:176px;top:1060px" width="26" height="26" viewBox="0 0 26 26"><rect x="4" y="4" width="18" height="18" fill="none" stroke="#f26a1b" stroke-width="1.5"/><path d="M8 13l4 4 6-8" stroke="#f26a1b" stroke-width="1.5" fill="none"/></svg>
  <svg class="pi-icon" style="left:382px;top:962px" width="26" height="26" viewBox="0 0 26 26"><circle cx="13" cy="13" r="9" fill="none" stroke="#f26a1b" stroke-width="1.5" stroke-dasharray="3 3"/><circle cx="13" cy="13" r="3" fill="#f26a1b"/></svg>
  <svg class="pi-icon" style="left:382px;top:1014px" width="26" height="26" viewBox="0 0 26 26"><path d="M4 20l7-7 4 4 7-9" stroke="#f26a1b" stroke-width="1.5" fill="none"/><circle cx="20" cy="18" r="4" fill="none" stroke="#f26a1b" stroke-width="1.5"/></svg>

  <h2 class="sec-title" style="left:0;width:585px;text-align:center;top:1176px;font-size:16px">3 Simple Ways to Get Your Estimate Today!</h2>
  <div class="abs" style="left:43px;top:1233px;font-family:'Oswald',sans-serif;font-size:8px;color:var(--ink)">WE MAKE THE PROCESS QUICK &amp; EASY</div>

  <div class="step-num" style="left:43px;top:1260px;font-size:22px">01</div>
  <div class="step" style="left:81px;top:1264px;width:100px"><h5>Call Us</h5><p class="tiny">Call us today and talk to one of our friendly, local staff members.</p></div>
  <div class="btn red" style="left:197px;top:1267px;width:56px;height:15px;font-size:4.5px">Click to Call</div>

  <div class="step-num" style="left:43px;top:1312px;font-size:22px">02</div>
  <div class="step" style="left:81px;top:1316px;width:100px"><h5>Text Us</h5><p class="tiny">Text Us today with photos of the stuff you would like removed.</p></div>
  <div class="btn amber" style="left:197px;top:1319px;width:56px;height:15px;font-size:4.5px">Click to Text</div>

  <div class="step-num" style="left:43px;top:1365px;font-size:22px">03</div>
  <div class="step" style="left:81px;top:1369px;width:100px"><h5>Email Us</h5><p class="tiny">Email us today what you would like us to remove.</p></div>
  <div class="btn red" style="left:197px;top:1372px;width:56px;height:15px;font-size:4.5px">Click to Email</div>

  <div class="deco-hex hex" style="left:420px;top:1209px;width:200px;height:215px"></div>
  <div class="photo truck-photo" style="left:281px;top:1270px;width:240px;height:130px;background:linear-gradient(180deg,transparent 0%,#9d8f80 15%,#1f1f22 30%,#1f1f22 70%,#777 100%);clip-path:polygon(0 30%,40% 10%,100% 10%,100% 90%,0 90%)" role="img" aria-label="Photo of the branded box truck loaded with furniture, showing the phone number and services on its side"></div>

  <div class="photo truck-photo hexv" style="left:42px;top:1439px;width:231px;height:216px;background:linear-gradient(180deg,#3a6fd1 0%,#9eb8e0 30%,#2a2a2d 55%,#4d5036 100%)" role="img" aria-label="Photo of a crew member standing next to the company box truck"></div>
  <h2 class="sec-title" style="left:302px;top:1484px;font-size:16px;line-height:1.2">Bigger Truck, Better<br>Pricing!</h2>
  <p class="body-copy" style="left:302px;top:1552px;width:215px">Bright Creek Junk Out is a local family owned and operated business and not a large national franchise. That means we don't have to pass along the 10-15% franchise fee on to our customers like our competitors.</p>

  <div class="compare" style="left:43px;top:1680px">
    <div class="truck" style="width:62px;height:30px" role="img" aria-label="Photo of the company box truck"></div>
    <div class="spec" style="font-size:5.5px;margin-left:18px">7 Pickup Loads<br>506 Cubic Feet<br>21 Cubic Yards</div>
  </div>
  <div class="vdiv" style="left:150px;top:1674px;height:43px"></div>
  <div class="compare" style="left:243px;top:1680px">
    <div class="truck" style="width:55px;height:28px;background:linear-gradient(180deg,#eee,#c4242a 50%,#222)" role="img" aria-label="Photo of a competitor's red truck"></div>
    <div class="spec" style="font-size:5.5px;margin-left:12px">6 Pickup Loads<br>480 Cubic Feet<br>18 Cubic Yards</div>
  </div>
  <div class="vdiv" style="left:397px;top:1674px;height:43px"></div>
  <div class="compare" style="left:422px;top:1680px">
    <div class="truck" style="width:55px;height:28px;background:linear-gradient(180deg,#eee,#2a49b0 50%,#222)" role="img" aria-label="Photo of a competitor's blue truck"></div>
    <div class="spec" style="font-size:5.5px;margin-left:12px">5 Pickup Loads<br>400 Cubic Feet<br>15 Cubic Yards</div>
  </div>

  <h2 class="sec-title" style="left:86px;top:1804px;font-size:17px">Service Areas</h2>
  <p class="body-copy" style="left:86px;top:1850px;width:180px">Bright Creek Junk Out offers junk removal and hauling services in most of the Bright Creek Valley.</p>
  <ul class="area-list" style="left:86px;top:1882px"><li>Boise</li><li>Meridian</li><li>Eagle</li><li>Star</li><li>Nampa</li></ul>
  <ul class="area-list" style="left:145px;top:1882px"><li>Caldwell</li><li>Middleton</li><li>Garden City</li><li>Kuna</li><li>Emmett</li></ul>
  <div class="link-orange" style="left:86px;top:1946px">View Location</div>
  <div class="photo map-photo hexv" style="left:292px;top:1771px;width:210px;height:215px" role="img" aria-label="Street map of the service region with the office location marked"></div>
  <div class="pin-hex hexv" style="left:425px;top:1930px;width:52px;height:58px">
    <svg width="16" height="20" viewBox="0 0 16 20"><path d="M8 1a6 6 0 0 0-6 6c0 4.5 6 12 6 12s6-7.5 6-12a6 6 0 0 0-6-6z" fill="none" stroke="#fff" stroke-width="2"/><circle cx="8" cy="7" r="2.2" fill="#fff"/></svg>
  </div>

  <div class="dark-band" style="top:2081px;width:585px;height:224px"></div>
  <div class="cta-band" style="left:43px;top:2042px;width:497px;height:78px"></div>
  <span class="abs" style="left:97px;top:2070px;width:40px;height:1px;background:#fff"></span>
  <div class="cta-text" style="left:148px;top:2060px;font-size:16px">Book service now same &amp; next<br>day service available!</div>
  <div class="btn-white" style="left:406px;top:2070px;width:83px;height:23px;font-size:6.5px">Contact Us</div>

  <div class="logo-text" style="left:56px;top:2188px;width:100px;font-size:15px">BRIGHT CREEK<br>JUNK OUT</div>
  <div class="foot-col" style="left:185px;top:2164px;font-size:6px"><h6 style="font-size:8px">Quick Links</h6><ul><li>Home</li><li>Service</li><li>How We Price</li><li>Make The Process</li><li>Service Area</li><li>Contact</li></ul></div>
  <div class="foot-col" style="left:289px;top:2164px;font-size:6px"><h6 style="font-size:8px">Our Service</h6><ul><li>Junk Removal &amp; Hauling</li><li>Property Cleanout</li><li>Light Demolition</li><li>Dumpster Rental</li></ul></div>
  <div class="foot-col" style="left:402px;top:2164px;font-size:7px"><h6 style="font-size:8px">Contact Us</h6>
    <div class="contact-row"><svg width="12" height="12" viewBox="0 0 24 24"><circle cx="12" cy="12" r="11" fill="#fff"/><path transform="translate(5 5) scale(.6)" fill="#2e2e2e" d="M6.6 10.8a15.2 15.2 0 0 0 6.6 6.6l2.2-2.2c.3-.3.7-.4 1-.2 1.1.4 2.3.6 3.6.6.6 0 1 .4 1 1V20c0 .6-.4 1-1 1A17 17 0 0 1 3 4c0-.6.4-1 1-1h3.5c.6 0 1 .4 1 1 0 1.3.2 2.5.6 3.6.1.3 0 .7-.2 1z"/></svg><div><small style="font-size:5px">Call*</small>+1 (208) 555-0147</div></div>
    <div class="contact-row"><svg width="12" height="12" viewBox="0 0 24 24"><circle cx="12" cy="12" r="11" fill="#fff"/><path d="M12 6v6l4 2" stroke="#2e2e2e" stroke-width="2" fill="none"/></svg><div><small style="font-size:5px">Hours*</small>Mon to Sat – 8 AM to 6 PM</div></div>
  </div>
  <div class="copyright" style="top:2288px;font-size:6px">© 2021 Bright Creek Junk Out. All rights reserved.</div>
  <div class="to-top" style="left:552px;top:2264px;width:25px;height:25px"><svg width="10" height="10" viewBox="0 0 10 10"><path d="M2 6l3-3 3 3" stroke="#fff" stroke-width="1.5" fill="none"/></svg></div>
</section>

<!-- ================= MOBILE ================= -->
<section class="frame mobile">
  <div class="photo hero-photo" style="left:0;top:0;width:161px;height:252px;background:linear-gradient(180deg,#e2e9f3 0%,#d2deed 40%,#aab6c4 62%,#3a3d43 78%,#5f6a4c 92%,#7b8456 100%)" role="img" aria-label="Photo of the company trucks and dumpster trailer parked in a row"></div>

  <div class="call-label abs" style="left:0;width:161px;text-align:center;top:8px;font-size:5px">CLICK TO CALL</div>
  <div class="phone-pill" style="left:30px;top:18px;width:99px;height:21px;font-size:9px">
    <span class="ic" style="width:15px;height:15px;margin:0 9px 0 3px">
      <svg width="9" height="9" viewBox="0 0 24 24"><path fill="#f26a1b" d="M6.6 10.8a15.2 15.2 0 0 0 6.6 6.6l2.2-2.2c.3-.3.7-.4 1-.2 1.1.4 2.3.6 3.6.6.6 0 1 .4 1 1V20c0 .6-.4 1-1 1A17 17 0 0 1 3 4c0-.6.4-1 1-1h3.5c.6 0 1 .4 1 1 0 1.3.2 2.5.6 3.6.1.3 0 .7-.2 1z"/></svg>
    </span>208-555-0147
  </div>
  <div class="burger abs" style="left:7px;top:50px;width:14px"><span style="margin-bottom:3px;height:1.5px"></span><span style="margin-bottom:3px;height:1.5px;width:10px"></span><span style="height:1.5px"></span></div>
  <div class="hours abs" style="left:42px;top:52px;font-size:5px">MON TO SAT 8AM TO 6PM</div>
  <div class="logo-text on-light" style="left:20px;top:98px;width:121px;font-size:15px">BRIGHT CREEK<br>JUNK OUT</div>

  <div class="banner" style="left:4px;top:272px;width:152px;height:74px;font-size:10px;line-height:1.3;padding:0 8px">Best rated junk removal &amp; property cleanout company in the Bright Creek Valley</div>

  <div class="review-mark" style="left:19px;top:366px;width:22px;height:22px"></div>
  <div class="review-name" style="left:48px;top:366px;font-size:9px">Localy<br>Business Review</div>
  <div class="score" style="left:19px;top:393px;font-size:11px">5.0</div>
  <div class="stars" style="left:48px;top:395px;font-size:8px">★★★★<span style="color:#ddd">★</span></div>
  <div class="pill-dark" style="left:7px;top:415px;width:149px;height:17px;line-height:17px;font-size:5.5px">Fast, friendly &amp; professionals...</div>
  <div class="rule" style="left:4px;top:450px;width:152px"></div>

  <div class="dark-band" style="top:780px;width:161px;height:356px"></div>

  <article class="card" style="left:4px;top:478px;width:120px;height:286px">
    <h4>Junk Removal</h4>
    <svg class="cicon" width="22" height="14" viewBox="0 0 22 14"><rect x="1" y="3" width="12" height="7" fill="none" stroke="#2b2b2b"/><path d="M13 5h5l3 3v2h-8z" fill="none" stroke="#2b2b2b"/><circle cx="5" cy="11.5" r="1.8" fill="#f26a1b"/><circle cx="17" cy="11.5" r="1.8" fill="#f26a1b"/></svg>
    <div class="cphoto" role="img" aria-label="Photo of old appliances set out for pickup"></div>
    <ul><li>Misc. Household Junk</li><li>Furniture Removal</li><li>Mattress Removal</li><li>Appliance Removal</li><li>Hot Tub Removal</li><li>Yard Debris Removal</li><li>Remodeling Debris</li><li>Construction Debris</li><li>Play Structure Removal</li><li>Shed Removal</li></ul>
    <div class="cbtn">Same &amp; next day<br>service available</div>
  </article>
  <article class="card" style="left:134px;top:478px;width:120px;height:286px">
    <h4>Property Cleanout</h4>
    <div class="cphoto" style="background:linear-gradient(170deg,#b9c4cf,#8b7d6c 55%,#5b4b3c)" role="img" aria-label="Photo of a house yard piled with items from a cleanout"></div>
    <ul><li>Estate Cleanout</li><li>Residential Cleanout</li><li>Garage Cleanout</li><li>Storage Unit Cleanout</li><li>Foreclosure Cleanout</li><li>Hoarder Cleanout</li><li>Attic Cleanout</li><li>Basement Cleanout</li><li>Business Cleanout</li><li>Office Cleanout</li><li>Mobile Home Cleanout</li><li>House Cleanout</li></ul>
    <div class="cbtn">We do all the hard work</div>
  </article>

  <div class="arrow-btn" style="left:59px;top:793px"><svg width="7" height="7" viewBox="0 0 10 10"><path d="M6 2L3 5l3 3" stroke="#555" stroke-width="1.5" fill="none"/></svg></div>
  <div class="arrow-btn" style="left:85px;top:793px"><svg width="7" height="7" viewBox="0 0 10 10"><path d="M4 2l3 3-3 3" stroke="#555" stroke-width="1.5" fill="none"/></svg></div>

  <h2 class="sec-title on-dark" style="left:0;width:161px;text-align:center;top:826px;font-size:12px">How We Price</h2>

  <svg class="pi-icon" style="left:6px;top:862px" width="24" height="24" viewBox="0 0 26 26"><rect x="3" y="5" width="20" height="16" fill="none" stroke="#f26a1b" stroke-width="1.5"/><path d="M7 10h12M7 14h8" stroke="#f26a1b" stroke-width="1.5"/></svg>
  <div class="price-item" style="left:38px;top:864px;width:118px"><h5 style="font-size:6px">Volume Based Pricing</h5><p style="font-size:5px">Our pricing is based on the amount of space your items take up in our truck.</p></div>
  <svg class="pi-icon" style="left:6px;top:908px" width="24" height="24" viewBox="0 0 26 26"><circle cx="13" cy="13" r="9" fill="none" stroke="#f26a1b" stroke-width="1.5"/><path d="M13 8v10M10 11h6" stroke="#f26a1b" stroke-width="1.5"/></svg>
  <div class="price-item" style="left:38px;top:910px;width:118px"><h5 style="font-size:6px">Free Estimates</h5><p style="font-size:5px">We can provide a free estimate over the phone, text or email so you know a price range before we show up.</p></div>
  <svg class="pi-icon" style="left:6px;top:961px" width="24" height="24" viewBox="0 0 26 26"><rect x="4" y="4" width="18" height="18" fill="none" stroke="#f26a1b" stroke-width="1.5"/><path d="M8 13l4 4 6-8" stroke="#f26a1b" stroke-width="1.5" fill="none"/></svg>
  <div class="price-item" style="left:38px;top:963px;width:118px"><h5 style="font-size:6px">No Hidden Fees</h5><p style="font-size:5px">All fuel, labor and disposal fees are included in your upfront pricing.</p></div>
  <svg class="pi-icon" style="left:6px;top:1005px" width="24" height="24" viewBox="0 0 26 26"><circle cx="13" cy="13" r="9" fill="none" stroke="#f26a1b" stroke-width="1.5" stroke-dasharray="3 3"/><circle cx="13" cy="13" r="3" fill="#f26a1b"/></svg>
  <div class="price-item" style="left:38px;top:1007px;width:118px"><h5 style="font-size:6px">Minimum Loads</h5><p style="font-size:5px">Our pricing starts at a minimum pickup fee and goes up through twelve different price points to a full load rate.</p></div>
  <svg class="pi-icon" style="left:6px;top:1057px" width="24" height="24" viewBox="0 0 26 26"><path d="M4 20l7-7 4 4 7-9" stroke="#f26a1b" stroke-width="1.5" fill="none"/><circle cx="20" cy="18" r="4" fill="none" stroke="#f26a1b" stroke-width="1.5"/></svg>
  <div class="price-item" style="left:38px;top:1059px;width:118px"><h5 style="font-size:6px">Upfront Pricing</h5><p style="font-size:5px">We always provide our valued customers with a firm price on-site before we begin a job.</p></div>

  <h2 class="sec-title" style="left:0;width:161px;text-align:center;top:1160px;font-size:11.5px;line-height:1.25">3 Simple Ways to Get Your<br>Estimate Today!</h2>
  <div class="abs" style="left:4px;top:1218px;font-family:'Oswald',sans-serif;font-size:6.5px;color:var(--ink)">WE MAKE THE PROCESS QUICK &amp; EASY</div>

  <div class="step-num" style="left:4px;top:1236px;font-size:16px">01</div>
  <div class="step" style="left:31px;top:1239px;width:120px"><h5 style="font-size:6.5px">Call Us</h5><p class="tiny">Call us today and talk to one of our friendly, local staff members.</p></div>
  <div class="btn red" style="left:31px;top:1274px;width:57px;height:14px;font-size:4.5px">Click to Call</div>
  <div class="step-num" style="left:4px;top:1308px;font-size:16px">02</div>
  <div class="step" style="left:31px;top:1311px;width:120px"><h5 style="font-size:6.5px">Text Us</h5><p class="tiny">Text Us today with photos of the stuff you would like removed.</p></div>
  <div class="btn amber" style="left:31px;top:1346px;width:57px;height:14px;font-size:4.5px">Click to Text</div>
  <div class="step-num" style="left:4px;top:1378px;font-size:16px">03</div>
  <div class="step" style="left:31px;top:1381px;width:120px"><h5 style="font-size:6.5px">Email Us</h5><p class="tiny">Email us today what you would like us to remove.</p></div>
  <div class="btn red" style="left:31px;top:1417px;width:57px;height:14px;font-size:4.5px">Click to Email</div>

  <div class="deco-hex hex" style="left:95px;top:1432px;width:110px;height:128px"></div>
  <div class="photo truck-photo" style="left:4px;top:1468px;width:150px;height:82px;background:linear-gradient(180deg,transparent 0%,#9d8f80 15%,#1f1f22 30%,#1f1f22 70%,#777 100%);clip-path:polygon(0 30%,40% 10%,100% 10%,100% 90%,0 90%)" role="img" aria-label="Photo of the branded box truck loaded with furniture"></div>

  <h2 class="sec-title" style="left:4px;top:1580px;font-size:11.5px;line-height:1.2">Bigger Truck, Better<br>Pricing!</h2>
  <p class="body-copy" style="left:4px;top:1622px;width:154px;font-size:5px">Bright Creek Junk Out is a local family owned and operated business and not a large national franchise. That means we don't have to pass along the 10-15% franchise fee on to our customers like our competitors.</p>
  <div class="photo truck-photo hexv" style="left:6px;top:1668px;width:148px;height:150px;background:linear-gradient(180deg,#3a6fd1 0%,#9eb8e0 30%,#2a2a2d 55%,#4d5036 100%)" role="img" aria-label="Photo of a crew member next to the company box truck"></div>

  <div class="abs" style="left:6px;top:1832px;width:42px;height:18px;background:linear-gradient(180deg,#eee,#555 60%,#222)" role="img" aria-label="Photo of the company box truck"></div>
  <div class="abs" style="left:61px;top:1832px;width:42px;height:18px;background:linear-gradient(180deg,#eee,#c4242a 50%,#222)" role="img" aria-label="Photo of a competitor's red truck"></div>
  <div class="abs" style="left:116px;top:1832px;width:42px;height:18px;background:linear-gradient(180deg,#eee,#2a49b0 50%,#222)" role="img" aria-label="Photo of a competitor's blue truck"></div>
  <div class="compare" style="left:10px;top:1855px"><div class="spec" style="font-size:4px">7 Pickup Loads<br>506 Cubic Feet<br>21 Cubic Yards</div></div>
  <div class="compare" style="left:65px;top:1855px"><div class="spec" style="font-size:4px">6 Pickup Loads<br>480 Cubic Feet<br>18 Cubic Yards</div></div>
  <div class="compare" style="left:120px;top:1855px"><div class="spec" style="font-size:4px">5 Pickup Loads<br>400 Cubic Feet<br>15 Cubic Yards</div></div>

  <h2 class="sec-title" style="left:4px;top:1918px;font-size:11.5px">Service Areas</h2>
  <p class="body-copy" style="left:4px;top:1943px;width:150px;font-size:5px">Bright Creek Junk Out offers junk removal and hauling services in most of the Bright Creek Valley.</p>
  <ul class="area-list" style="left:4px;top:1980px"><li style="font-size:5.5px">Boise</li><li style="font-size:5.5px">Meridian</li><li style="font-size:5.5px">Eagle</li><li style="font-size:5.5px">Star</li><li style="font-size:5.5px">Nampa</li></ul>
  <ul class="area-list" style="left:66px;top:1980px"><li style="font-size:5.5px">Caldwell</li><li style="font-size:5.5px">Middleton</li><li style="font-size:5.5px">Garden City</li><li style="font-size:5.5px">Kuna</li><li style="font-size:5.5px">Emmett</li></ul>
  <div class="link-orange" style="left:4px;top:2055px;font-size:5px">View Location</div>
  <div class="photo map-photo hexv" style="left:4px;top:2068px;width:154px;height:190px" role="img" aria-label="Street map of the service region with the office location marked"></div>
  <div class="pin-hex hexv" style="left:100px;top:2216px;width:42px;height:48px">
    <svg width="13" height="16" viewBox="0 0 16 20"><path d="M8 1a6 6 0 0 0-6 6c0 4.5 6 12 6 12s6-7.5 6-12a6 6 0 0 0-6-6z" fill="none" stroke="#fff" stroke-width="2"/><circle cx="8" cy="7" r="2.2" fill="#fff"/></svg>
  </div>

  <div class="dark-band" style="top:2322px;width:161px;height:486px"></div>
  <div class="cta-band" style="left:4px;top:2267px;width:152px;height:113px"></div>
  <div class="cta-text" style="left:4px;width:152px;text-align:center;top:2282px;font-size:11px">Book service now<br>same &amp; next day service<br>available!</div>
  <div class="btn-white" style="left:41px;top:2340px;width:78px;height:19px;font-size:5.5px">Contact Us</div>

  <div class="logo-text" style="left:4px;top:2428px;width:92px;font-size:12px;text-align:left">BRIGHT CREEK<br>JUNK OUT</div>
  <div class="foot-col" style="left:4px;top:2498px;font-size:5.5px"><h6 style="font-size:6.5px">Quick Links</h6><ul><li>Home</li><li>Service</li><li>How We Price</li><li>Make The Process</li><li>Service Area</li><li>Contact</li></ul></div>
  <div class="foot-col" style="left:4px;top:2598px;font-size:5.5px"><h6 style="font-size:6.5px">Our Service</h6><ul><li>Junk Removal &amp; Hauling</li><li>Property Cleanout</li><li>Light Demolition</li><li>Dumpster Rental</li></ul></div>
  <div class="foot-col" style="left:4px;top:2673px;font-size:6.5px"><h6 style="font-size:6.5px">Contact Us</h6>
    <div class="contact-row"><svg width="11" height="11" viewBox="0 0 24 24"><circle cx="12" cy="12" r="11" fill="#fff"/><path transform="translate(5 5) scale(.6)" fill="#2e2e2e" d="M6.6 10.8a15.2 15.2 0 0 0 6.6 6.6l2.2-2.2c.3-.3.7-.4 1-.2 1.1.4 2.3.6 3.6.6.6 0 1 .4 1 1V20c0 .6-.4 1-1 1A17 17 0 0 1 3 4c0-.6.4-1 1-1h3.5c.6 0 1 .4 1 1 0 1.3.2 2.5.6 3.6.1.3 0 .7-.2 1z"/></svg><div><small style="font-size:4.5px">Call*</small>+1 (208) 555-0147</div></div>
    <div class="contact-row"><svg width="11" height="11" viewBox="0 0 24 24"><circle cx="12" cy="12" r="11" fill="#fff"/><path d="M12 6v6l4 2" stroke="#2e2e2e" stroke-width="2" fill="none"/></svg><div><small style="font-size:4.5px">Hours*</small>Mon to Sat – 8 AM to 6 PM</div></div>
  </div>
  <div class="to-top" style="left:69px;top:2768px;width:22px;height:22px"><svg width="9" height="9" viewBox="0 0 10 10"><path d="M2 6l3-3 3 3" stroke="#fff" stroke-width="1.5" fill="none"/></svg></div>
  <div class="copyright" style="top:2796px;font-size:4.5px">© 2021 Bright Creek Junk Out. All rights reserved.</div>
</section>

</body>
</html>
```